Retail and Ecommerce Archery Shop needs new Home Page Design

We need a homepage design created for an existing company named Redhollow Bowsport Hub. They sell various types of Archery equipment for both Bow hunting and Target shooting both in store and online. They offer shooting lessons, have an indoor archery shooting range with memberships available, and have their own line of bowstrings. For color scheme, use the current home page as inspiration. The Homepage Template has links to specific images, if any other images are needed, stock images are acceptable.

Current Website: https://rhbowsporthub.com/

Customer Avatar: https://files.quillnest.net/page/d/4Tq8Wm2RbXk9LpZ3vNc7HyF1gJd6sKe5uA0oVtB2/view?mode=shared

Core Message Canvas: https://files.quillnest.net/tables/d/7Hm_482rTz906R3k21wLuNy8Pq0Zc47bd5jS2X_vW/view?mode=shared

Homepage Template-Use this worksheet as the structue of the homepage: https://files.quillnest.net/page/d/9xkpWvRfa2B5nT7eLcM3JsYq0HdG8oUiZbN4/view?mode=shared

```html
<!DOCTYPE html>
<html lang="en">
<head>
<meta charset="utf-8">
<title>Redhollow Bowsport Hub — Home</title>
<link href="https://fonts.googleapis.com/css2?family=Lora:wght@400;500&family=Nunito+Sans:wght@400;600;700;800&display=swap" rel="stylesheet">
<style>
:root{
  --gold:#f5cf0f;
  --ink:#141414;
  --text:#2b2b2b;
  --muted:#555;
  --paper:#ffffff;
  --mist:#efefef;
  --night:#1c1c1c;
  --forest-1:#2d3324;
}
*{box-sizing:border-box;margin:0;padding:0}
html,body{width:1200px;height:3521px;overflow:hidden}
body{font-family:'Nunito Sans',sans-serif;color:var(--text);background:var(--paper);position:relative}
section,header,footer{position:absolute;left:0;width:1200px}
.abs{position:absolute}
.center{text-align:center;left:0;width:1200px}

/* hero */
.hero{top:0;height:680px;background:radial-gradient(ellipse at 45% 35%,#6b6456 0%,#3a3a30 40%,#22241d 75%),var(--forest-1);overflow:hidden}
.hero-photo{position:absolute;inset:0;background:linear-gradient(180deg,rgba(0,0,0,.15),rgba(40,30,60,.45))}
.brand{left:133px;top:44px;display:flex;align-items:center;gap:10px}
.brand-dot{width:22px;height:22px;border-radius:50%;background:var(--gold)}
.brand-name{font-family:'Lora',serif;font-size:20px;color:var(--gold);white-space:nowrap}
.nav{top:20px;right:133px;display:flex;gap:33px;font-family:'Lora',serif;font-size:16px;color:#fff}
.hero h1{top:308px;font-family:'Lora',serif;font-weight:400;font-size:50px;line-height:58px;color:#fff}
.perks{top:452px;left:283px;width:605px;height:52px;border-top:2px solid rgba(255,255,255,.75);border-bottom:2px solid rgba(255,255,255,.75);display:flex;justify-content:center;align-items:center;gap:40px;font-weight:800;font-size:18px;color:#fff}
.perks span::before{content:"";display:inline-block;width:11px;height:11px;border-radius:50%;background:var(--gold);margin-right:9px;vertical-align:1px}
.btn{display:flex;align-items:center;justify-content:center;font-family:'Lora',serif;font-size:16px;color:var(--ink);background:var(--gold)}
.hero .btn{top:554px;width:208px;height:46px}

/* brands */
.pro{top:680px;height:428px}
.sec-title{font-family:'Lora',serif;font-weight:500;font-size:28px;color:var(--ink)}
.rule{position:absolute;left:570px;width:60px;height:3px;background:var(--gold)}
.badges{left:133px;width:934px;display:flex;justify-content:space-between;align-items:center}
.badge{background:#d9d9d9;border-radius:6px}
.pro p{top:295px;left:245px;width:710px;text-align:center;font-family:'Lora',serif;font-size:16px;line-height:26px;color:var(--text)}

/* bowstrings */
.strings{top:1108px;height:694px;background:var(--gold)}
.video{left:151px;top:150px;width:899px;height:422px;background:linear-gradient(100deg,#6f6f6b 0%,#3b3b3e 35%,#8a8a84 65%,#5d7a4a 100%)}
.strings .btn{top:603px;left:465px;width:271px;height:49px;background:#fff}

/* welcome */
.welcome{top:1802px;height:886px}
.welcome .sub{top:104px;font-family:'Lora',serif;font-size:21px;color:var(--text)}
.welcome-photo{left:133px;top:235px;width:420px;height:477px;background:linear-gradient(160deg,#6d5a2e 0%,#3f4a2c 45%,#2f3a26 100%)}
.feature{left:587px;width:480px;display:flex;gap:25px}
.feature .ico{flex:0 0 83px;height:83px;border-radius:50%;background:var(--gold);display:flex;align-items:center;justify-content:center}
.feature h3{font-family:'Lora',serif;font-weight:400;font-size:16px;line-height:19px;color:var(--ink);margin-bottom:14px}
.feature p{font-size:12px;line-height:17.5px;color:var(--muted)}
.welcome .btn{top:773px;left:509px;width:183px;height:48px}

/* newsletter */
.news{top:2688px;height:380px;background:linear-gradient(180deg,#f1f1f1,#e7e7e7)}
.news h2{top:68px;font-family:'Lora',serif;font-weight:500;font-size:29px;line-height:39px;color:var(--ink)}
.news p{top:164px;font-family:'Lora',serif;font-size:19px;line-height:29px;color:var(--text)}
.signup{top:248px;left:303px;width:595px;height:55px;display:flex;border:2px solid var(--gold);background:#fff}
.signup .field{flex:1;display:flex;align-items:center;gap:14px;padding-left:18px;font-size:14px;color:var(--ink)}
.signup .go{width:130px;background:var(--gold);display:flex;align-items:center;justify-content:center;font-family:'Lora',serif;font-size:17px;color:var(--ink)}

/* footer */
.foot{top:3068px;height:453px;background:var(--night);color:#fff}
.foot .brand{top:92px}
.col h4{font-size:13px;font-weight:800;letter-spacing:.3px;padding-bottom:10px;border-bottom:2px solid #ddd}
.col .row{display:flex;align-items:flex-start;gap:10px;margin-top:22px;font-size:12px;line-height:16px;white-space:nowrap}
.dot{flex:0 0 24px;height:24px;border-radius:50%;background:var(--gold);display:flex;align-items:center;justify-content:center}
.menu a{display:block;color:#fff;text-decoration:none;font-size:12px;line-height:19px}
.misc{top:282px;left:130px;width:935px;height:82px;border-top:2px solid #ddd;border-bottom:2px solid #ddd;display:flex;align-items:center;gap:24px}
.misc b{font-size:12px;font-weight:800;white-space:nowrap}
.misc span{font-size:12px;line-height:17px;color:#eee}
.legal{top:405px;font-size:11px;color:#eee}
</style>
</head>
<body>

<header class="hero">
  <div class="hero-photo" role="img" aria-label="Bow hunter drawing a compound bow among forest trees and wildflowers"></div>
  <div class="abs brand"><span class="brand-dot"></span><span class="brand-name">Redhollow Bowsport Hub</span></div>
  <nav class="abs nav"><span>Shop</span><span>About Us</span><span>Range</span><span>Pro Shop</span><span>Electric Bowstrings</span></nav>
  <h1 class="abs center">Your Bow Hunting<br>Adventure Starts Here!</h1>
  <div class="abs perks"><span>Top-Notch Equipment</span><span>Expertise</span><span>Unmatched Support</span></div>
  <a class="abs btn" style="left:377px">Indoor Archery Range</a>
  <a class="abs btn" style="left:602px">Shop Our Bows</a>
</header>

<section class="pro">
  <h2 class="abs center sec-title" style="top:74px">We Are a Full-Service Archery Pro Shop</h2>
  <div class="rule" style="top:140px"></div>
  <div class="abs badges" style="top:200px">
    <div class="badge" style="width:88px;height:40px"></div>
    <div class="badge" style="width:106px;height:44px;border-radius:50%"></div>
    <div class="badge" style="width:122px;height:40px"></div>
    <div class="badge" style="width:156px;height:44px"></div>
    <div class="badge" style="width:56px;height:56px"></div>
    <div class="badge" style="width:110px;height:36px"></div>
  </div>
  <p class="abs">Our services include Bow setup and sizing, D-loop and peep sight installs, accessory installs, and setup, cam/limb swaps, string swaps, paper tuning, 2nd/3rd axis adjustments, replacement parts, arrow building, tuning, and much more!</p>
</section>

<section class="strings">
  <h2 class="abs center sec-title" style="top:40px">Our Custom Electric Bowstrings</h2>
  <div class="rule" style="top:102px;background:var(--ink)"></div>
  <div class="abs video" role="img" aria-label="Video still of a bow sight and orange bowstring close up"></div>
  <svg class="abs" style="left:586px;top:347px" width="36" height="42" viewBox="0 0 36 42"><path d="M0 0 36 21 0 42Z" fill="#fff"/></svg>
  <a class="abs btn">Shop Our Custom Bowstrings</a>
</section>

<section class="welcome">
  <h2 class="abs center sec-title" style="top:52px">Welcome to your local Archery Shop</h2>
  <div class="abs center sub">Where consistency is built</div>
  <div class="rule" style="top:163px"></div>
  <div class="abs welcome-photo" role="img" aria-label="Archer in camouflage aiming a crossbow in an autumn forest"></div>

  <div class="abs feature" style="top:248px">
    <div class="ico"><svg width="44" height="44" viewBox="0 0 44 44" fill="none" stroke="#141414" stroke-width="3"><path d="M8 36 38 6M30 6h8v8M10 8c14 2 24 12 26 26M8 10 34 36"/></svg></div>
    <div><h3>Looking for a new Bow setup?</h3><p>Our custom bow-fitting process will be perfect for you. We get you set up the right way, the first time! We will get your measurements, check your shot, and make sure you leave feeling confident with your new Bow!</p></div>
  </div>
  <div class="abs feature" style="top:398px">
    <div class="ico"><svg width="44" height="44" viewBox="0 0 44 44" fill="none" stroke="#141414" stroke-width="3.5"><circle cx="20" cy="24" r="16"/><circle cx="20" cy="24" r="8"/><path d="M20 24 38 6M32 6h6v6"/></svg></div>
    <div><h3>Looking to make some improvements to your current archery setup?</h3><p>We have access to almost all of the popular archery accessories on the market! We don't sell anything we wouldn't use ourselves so come on in and talk with our shop experts to figure out what will work best for you.</p></div>
  </div>
  <div class="abs feature" style="top:560px">
    <div class="ico"><svg width="46" height="46" viewBox="0 0 46 46" fill="none" stroke="#141414" stroke-width="3.5"><circle cx="23" cy="23" r="15"/><circle cx="23" cy="23" r="3" fill="#141414"/><path d="M23 2v12M23 32v12M2 23h12M32 23h12"/></svg></div>
    <div><h3>Are you looking to improve your shot?<br>Reserve some time on our range!</h3><p>Before you step into the field to take your first shot of the season, take time to go to the range. Archery, like any skill, requires practice &amp; diligence to develop a consistent &amp; confident shot. We have a 12-lane 20-yard indoor range in the shop. Daily Range and memberships are available. We also offer bow rental and lessons.</p></div>
  </div>
  <a class="abs btn">Range Informaiton</a>
</section>

<section class="news">
  <h2 class="abs center">Join Our Archery Community: Exclusive Deals,<br>Tips, and Updates Straight to Your Inbox!</h2>
  <p class="abs center">Join today &amp; stay up-to-date on new product releases,<br>shop promotions, and our archery newsletters</p>
  <div class="abs signup">
    <div class="field"><svg width="18" height="14" viewBox="0 0 18 14"><rect x="1" y="1" width="16" height="12" fill="none" stroke="#141414" stroke-width="2"/><path d="M1 1l8 7 8-7" fill="none" stroke="#141414" stroke-width="2"/></svg>Email id</div>
    <div class="go">Signup</div>
  </div>
</section>

<footer class="foot">
  <div class="abs brand"><span class="brand-dot"></span><span class="brand-name">Redhollow Bowsport Hub</span></div>

  <div class="abs col" style="left:402px;top:46px;width:192px">
    <h4>CONTACT US</h4>
    <div class="row"><span class="dot"><svg width="10" height="13" viewBox="0 0 10 13"><path d="M5 13S0 7 0 5a5 5 0 0110 0c0 2-5 8-5 8z" fill="#1c1c1c"/></svg></span><span>4120 W Prairie Rd. 17, Ashbury,<br>Redhollow 60418 USA</span></div>
    <div class="row"><span class="dot"><svg width="12" height="12" viewBox="0 0 12 12"><path d="M2 1l3 2-1 2c1 2 2 3 4 4l2-1 2 3-2 1C5 11 1 7 1 3z" fill="#1c1c1c"/></svg></span><span>Call Us<br>(555)-214-0387</span></div>
    <div class="row"><span class="dot"><svg width="12" height="9" viewBox="0 0 12 9"><rect width="12" height="9" fill="#1c1c1c"/><path d="M0 0l6 5 6-5" stroke="#f5cf0f" fill="none"/></svg></span><span>E mail Us<br>hello@rhbowsporthub.com</span></div>
  </div>

  <div class="abs col menu" style="left:713px;top:46px;width:107px">
    <h4>MENU</h4>
    <div style="margin-top:20px"><a>Shop</a><a>About Us</a><a>Range</a><a>Pro Shop</a><a>Electric Bowstrings</a></div>
  </div>

  <div class="abs col" style="left:961px;top:46px;width:106px">
    <h4>FOLLOW US</h4>
    <div class="row"><span class="dot"></span><span>Like us on<br>FRIENDGRID</span></div>
    <div class="row"><span class="dot"></span><span>Follow us on<br>CHIRPLINE</span></div>
    <div class="row"><span class="dot"></span><span>Follow us on<br>WORKNET</span></div>
  </div>

  <div class="abs misc"><b>Miscellaneous</b><span>Sed ut perspiciatis unde omnis iste natus error sit voluptatem accusantium doloremque laudantium, totam rem aperiam, eaque ipsa quae ab illo inventore veritatis et quasi architecto beatae vitae dicta sunt explicabo. Nemo enim ipsam voluptatem quia voluptas sit.</span></div>
  <div class="abs center legal">Terms of Service &nbsp; | &nbsp; Privacy Policy &nbsp; | &nbsp; Copyright © 2023 All Rights Reserved</div>
</footer>

</body>
</html>
```